Web Design for Solar Energy Consultancy Company

~ May 3, 2017 Update ~
As our project is rapidly progressing towards its completion, we started building up the list of designs that attracted the most of the team's attention. Additional submittals are still most welcome. Before submitting your proposal, however, we can recommend to review the concepts that received 4 stars as these are the ones that, in our opinion, most closely match the brief's requirements. Thank you!!
~ April 30, 2017 Update ~
The project deadline has been extended to attract a broader design community and to better tailor the final design to the requirements of the project.
A "light", "clean" (minimalistic), professionally looking, unique design is expected. Please, try to avoid industry cliches. Also, please use green, which became another industry cliche, with great caution. The brief provides minimum details to foster creativity. With the same notion in mind, the page content information is not provided.
Thank you for your feedback and support of the project!!
~ April 22, 2017 Update ~
Additional comments after starting receiving more designs:
- your attention to the brief's requirements will be highly appreciated. It is expected that the design is unique - standard, commonly used, images, formats and approaches do not fall under this category. There is no need to "bombard" with slightly different variations of the same design. It is expected that a conceptual (preliminary) design is submitted first, and, after it is reviewed (each design will receive a star rating and, if the star rating is greater than 3, a detailed feedback), the requested changes are implemented. We believe this will allow to approach the design process more efficiently and safe additional time to both the Designers's Community and our company. Thank you for understanding.
Clarification, please submit two variations of a design:
1) 1 page "business card" design that the company will be able to use during its startup stage;
2) the fully functional design (as per the requirements outlined below) for the company to transition to after the start-up period is over. Same design principles as developed for option 1 should be used for this variation.
Additional clarification, please note that the news block will not require images (at least during the start-up stage). It is envisioned to be a news feeder.
~ April 21, 2017 Update ~
Preliminary comments after receiving first designs:
- please try to create a unique design, using common elements wisely. Though such solar energy "attributes" as a solar panel or a bulb are very well recognized and allow quickly identify the nature of the business, they also became so common that in many cases a design may seem very similar to the one of others (Oh!, I've already seen this... effect).
- please try to introduce the company's logo unobtrusively. The size and position of the logo should clearly identify the company, but the message should be subtle, the logo should not distract from the main design. Zorb's swoosh did not need to occupy have the screen.
- please use the green color with caution as it was with the company's logo. True, it is a green energy. But there is no need for the color to "scream" about it. Use the amount of green and its tone (avoid acid green) wisely.
--------------------------------------------------------------------------------
1. Main Goal
Develop a website that can represent the company to the industry stakeholders and become its "business card" during the start-up stage.
2. Secondary Goal
Develop a structure of a fully functional website that the "business card" design can eventually be transformed to staying consistent with the original design principles.
3. Key Audience
Varluk Corp. is providing consulting and technical services in the area of Solar Energy. The industry stakeholders include project developers, financial community, governmental bodies, OEMs, and competition.
4. Site Map
- HOME
• About
• Services
• Solar Energy
• News
• Contacts
• Social Media
- SERVICES*
- PROJECTS*
- FINANCE*
- TRAINING*
- SOLAR (ENERGY)*
* Maybe inactive / partially functional during the start-up stage.
5. Technical Specifications
Online brochure website during the start-up stage with a capability to be eventually transformed to a fully functional website while preserving the original design principles.
The design to be appealing, "light", professional, and with an intuitive and easy to navigate interface. Modern coding principles supporting efficiency and security to be utilized. Newest industry trends in website coding will be welcome.
The website to be designed so that it would fit well a computer, tablet, or mobile phone screen of any size. Cross-platform functionality to be taken into consideration to ensure that the website is fully functional on any platform.
Company's logo has already been designed and will be shared with the short-listed designers during the final design stage.
6. Interaction
The website will provide information about the company, our services, and projects. In addition, the industry insight, accumulated knowledge, and most recent trends are planned to be shared with stakeholders and attract and retain the audience.
Interaction with designers during the website development is envisioned to go through the following steps:
a) conceptual design - to be proposed by a designer originally. All conceptual designs will be reviewed and a feedback provided to pre-selected designers;
b) (preliminary and) final design - depending on the level of additional changes required can be broken into two steps. After discussing preliminary designs, company images will be provided to the selected finalists, who will compete with their final proposals.
7. Industry Stakeholders
- https://www.brennowlet.com/power/solar-power.- http://www.plovaquenterm.com/
- http://www.kestrifolmwork.com/about/company/
- https://www.qatpor.com/energy/index.html
8. Budget
Defined by the project.
9. Timescale
Defined by the project.
12. Additional Info
- No copy-cats, standard graphics, or cliches please!
- Additional information / clarifications will be gladly provided upon request.
- This specification may be updated throughout the project to reflect discussions with / changes proposed by the Designers community.

```html
<!DOCTYPE html>
<html lang="en">
<head>
<meta charset="utf-8">
<title>Varluk Corp. — Solar Energy Consulting</title>
<link href="https://fonts.googleapis.com/css2?family=Poppins:wght@300;400;500;600;700&display=swap" rel="stylesheet">
<style>
:root{
  --green:#2f9e44;
  --orange:#f9a300;
  --ink:#222222;
  --body:#555555;
  --soft-bg:#f8f8f8;
  --white:#ffffff;
}
*{margin:0;padding:0;box-sizing:border-box}
html,body{width:1200px;height:2932px;overflow:hidden}
body{font-family:'Poppins',sans-serif;color:var(--body);background:var(--white);position:relative}
.section{position:absolute;left:0;width:1200px}
.btn{display:inline-block;background:var(--orange);color:var(--white);font-weight:500;border-radius:30px;text-align:center;text-decoration:none}

/* hero */
.hero{top:0;height:629px;overflow:hidden}
.hero-photo{position:absolute;inset:0;background:
  linear-gradient(90deg,rgba(20,45,110,.0) 0%,rgba(20,45,110,0) 100%),
  linear-gradient(115deg,#1d3f86 0%,#2a5bb0 30%,#3a6fc0 45%,#8fb3d8 55%,#bcd3ea 62%,#9fb96a 72%,#7ea53a 85%,#6a9430 100%)}
.hero-photo::after{content:"";position:absolute;inset:0;background:linear-gradient(180deg,rgba(255,255,255,0) 55%,rgba(70,110,30,.35) 100%)}
.nav{position:absolute;top:0;left:0;width:1200px;height:120px}
.brand{position:absolute;left:205px;top:42px;display:flex;align-items:center;gap:8px;color:var(--white);font-weight:600;font-size:26px;letter-spacing:1px}
.brand-dot{width:30px;height:30px;border-radius:50%;background:var(--orange)}
.nav-links{position:absolute;left:568px;top:60px;display:flex;gap:30px;list-style:none}
.nav-links li{color:var(--white);font-size:11px;font-weight:600;letter-spacing:.5px;padding-bottom:6px}
.nav-links li.active{border-bottom:2px solid var(--orange)}
.hero-copy{position:absolute;top:296px;left:0;width:1200px;text-align:center;color:var(--white);font-size:27px;font-weight:500;line-height:44px}
.hero .btn{position:absolute;left:518px;top:402px;width:162px;height:40px;line-height:40px;font-size:15px}
.dots{position:absolute;top:566px;left:564px;display:flex;gap:10px}
.dots span{width:8px;height:8px;border-radius:50%;background:rgba(255,255,255,.55)}
.dots span.on{background:var(--white)}

/* about */
.about{top:629px;height:512px;background:var(--white)}
.section-title{color:var(--green);font-weight:600;font-size:35px}
.about .section-title{position:absolute;left:197px;top:64px}
.about-text{position:absolute;left:197px;top:150px;width:395px;font-size:12.5px;line-height:23px}
.partners{position:absolute;left:199px;top:422px;display:flex;gap:26px;align-items:center}
.partner{height:26px;border-radius:3px;background:#d7dde3}
.partner.one{width:104px;background:#cfe0d6}
.partner.two{width:138px;background:#f1dcc8}
.partner.three{width:120px;background:#c9dcea}
.about-art{position:absolute;left:0;top:0}

/* services */
.services{top:1141px;height:516px;background:var(--soft-bg)}
.services .section-title{position:absolute;top:92px;width:1200px;text-align:center}
.service{position:absolute;top:200px;width:400px}
.service.solar{left:197px}
.service.consult{left:606px}
.service-head{display:flex;align-items:center;gap:14px;height:60px}
.service-head h3{color:var(--ink);font-size:28px;font-weight:600}
.service p{margin-top:28px;font-size:12.5px;line-height:23px}
.service .btn{margin-top:24px;width:113px;height:28px;line-height:28px;font-size:11px}

/* solar band */
.solar-band{top:1657px;height:450px;overflow:hidden}
.solar-photo{position:absolute;inset:0;background:linear-gradient(180deg,#3c4c5c 0%,#5d6670 30%,#6a6358 48%,#2d4a7e 60%,#1e3c72 80%,#17305c 100%)}
.solar-band .section-title{position:absolute;top:118px;width:1200px;text-align:center}
.solar-band p{position:absolute;left:305px;top:186px;width:590px;text-align:center;color:var(--white);font-size:13.5px;line-height:22px}
.solar-band .btn{position:absolute;left:518px;top:297px;width:162px;height:41px;line-height:41px;font-size:15px}

/* news */
.news{top:2107px;height:570px;background:var(--white)}
.news .section-title{position:absolute;top:62px;width:1200px;text-align:center}
.news-item{position:absolute;top:186px;width:272px}
.news-item:nth-of-type(1){left:199px}
.news-item:nth-of-type(2){left:471px}
.news-item:nth-of-type(3){left:744px}
.news-date{color:var(--ink);font-size:13px;font-weight:600}
.news-item h4{margin-top:18px;color:#333;font-size:20px;font-weight:300;line-height:23px}
.news-rule{margin-top:20px;width:48px;height:4px;background:var(--orange)}
.news-item p{margin-top:34px;font-size:12.5px;line-height:22px}

/* footer */
.footer{top:2677px;height:255px;background:var(--soft-bg)}
.footer-brand{position:absolute;left:197px;top:52px;display:flex;align-items:center;gap:8px;color:var(--ink);font-weight:600;font-size:26px;letter-spacing:1px}
.footer-col{position:absolute;top:56px;list-style:none;font-size:11px;font-weight:500;color:var(--ink);line-height:22.5px}
.footer-col.c1{left:463px}
.footer-col.c2{left:614px}
.footer-col.c3{left:770px}
.footer-bottom{position:absolute;top:216px;left:199px;width:790px;display:flex;justify-content:space-between;font-size:10.5px;font-weight:600;color:var(--ink)}
.social{display:flex;align-items:center;gap:10px}
.social i{width:9px;height:9px;border-radius:50%;background:#9aa3ad;display:inline-block}
.social i.first{background:var(--orange)}
</style>
</head>
<body>

<header class="section hero">
  <div class="hero-photo" role="img" aria-label="Photograph of solar panels in a green meadow under a sunny blue sky"></div>
  <nav class="nav">
    <div class="brand"><span class="brand-dot"></span>VARLUK</div>
    <ul class="nav-links">
      <li class="active">HOME</li><li>SERVICES</li><li>PROJECTS</li><li>FINANCE</li><li>TRAINING</li><li>SOLAR</li>
    </ul>
  </nav>
  <p class="hero-copy">Varluk Corp. is providing consulting and<br>technical services in the area of Solar Energy.</p>
  <a class="btn">Learn More</a>
  <div class="dots"><span class="on"></span><span></span><span></span></div>
</header>

<section class="section about">
  <svg class="about-art" width="1200" height="512" viewBox="0 0 1200 512">
    <defs>
      <linearGradient id="windGrey" x1="0" y1="0" x2="1" y2="1">
        <stop offset="0" stop-color="#e6e6e6"/>
        <stop offset=".45" stop-color="#b8b8b8"/>
        <stop offset="1" stop-color="#5a5a5a"/>
      </linearGradient>
    </defs>
    <polygon points="541,0 1200,0 1200,512 778,512" fill="var(--orange)"/>
    <polygon points="621,0 1200,0 1200,489 805,489" fill="url(#windGrey)" role="img" aria-label="Black and white photograph of solar panels and wind turbines"/>
  </svg>
  <h2 class="section-title">About</h2>
  <p class="about-text">Sed ut perspiciatis unde omnis iste natus error sit voluptatem accusantium doloremque laudantium, totam rem aperiam, eaque ipsa quae ab illo inventore veritatis et quasi architecto beatae vitae dicta sunt explicabo. Nemo enim ipsam voluptatem quia voluptas sit aspernatur aut odit aut fugit, sed quia consequuntur magni dolores eos qui ratione voluptatem sequi nesciunt. Neque porro quisquam est, qui dolorem ipsum quia dolor sit amet, consectetur, adipisci velit,</p>
  <div class="partners">
    <span class="partner one"></span><span class="partner two"></span><span class="partner three"></span>
  </div>
</section>

<section class="section services">
  <h2 class="section-title">Services</h2>
  <article class="service solar">
    <div class="service-head">
      <svg width="52" height="52" viewBox="0 0 52 52" fill="none" stroke="var(--orange)" stroke-width="2" stroke-linecap="round">
        <circle cx="26" cy="26" r="11"/>
        <path d="M26 3v7M26 42v7M3 26h7M42 26h7M9.7 9.7l5 5M37.3 37.3l5 5M9.7 42.3l5-5M37.3 14.7l5-5"/>
      </svg>
      <h3>Solar Energy</h3>
    </div>
    <p>Sed ut perspiciatis unde omnis iste natus error sit voluptatem accusantium doloremque laudantium, totam rem aperiam, eaque ipsa quae ab illo inventore veritatis et quasi architecto beatae vitae</p>
    <a class="btn">Read More</a>
  </article>
  <article class="service consult">
    <div class="service-head">
      <svg width="54" height="52" viewBox="0 0 54 52" fill="none" stroke="var(--orange)" stroke-width="2" stroke-linejoin="round">
        <path d="M27 4C13 4 3 12 3 23c0 6 3 11 8 14l-3 11 11-7c2.5.6 5 1 8 1 14 0 24-8 24-19S41 4 27 4z"/>
        <circle cx="18" cy="23" r="1.5" fill="var(--orange)"/><circle cx="27" cy="23" r="1.5" fill="var(--orange)"/><circle cx="36" cy="23" r="1.5" fill="var(--orange)"/>
      </svg>
      <h3>Consulting</h3>
    </div>
    <p>Sed ut perspiciatis unde omnis iste natus error sit voluptatem accusantium doloremque laudantium, totam rem aperiam, eaque ipsa quae ab illo inventore veritatis et quasi architecto beatae vitae</p>
    <a class="btn">Read More</a>
  </article>
</section>

<section class="section solar-band">
  <div class="solar-photo" role="img" aria-label="Photograph of rows of solar panels stretching to the horizon at dusk"></div>
  <h2 class="section-title">Solar Energy</h2>
  <p>Sed ut perspiciatis unde omnis iste natus error sit voluptatem accusantium doloremque laudantium, totam rem aperiam, eaque ipsa quae ab illo inventore veritatis et quasi architecto beatae vitae</p>
  <a class="btn">Learn More</a>
</section>

<section class="section news">
  <h2 class="section-title">News</h2>
  <article class="news-item">
    <div class="news-date">April 21th 2017</div>
    <h4>Sed ut perspiciatis unde omnis iste natus error sit voluptatem</h4>
    <div class="news-rule"></div>
    <p>Sed ut perspiciatis unde omnis iste natus error sit voluptatem accusantium doloremque laudantium, totam rem aperiam, eaque ipsa quae ab illo inventore veritatis et quasi architecto beatae vitae</p>
  </article>
  <article class="news-item">
    <div class="news-date">April 21th 2017</div>
    <h4>Sed ut perspiciatis unde omnis iste natus error sit voluptatem</h4>
    <div class="news-rule"></div>
    <p>Sed ut perspiciatis unde omnis iste natus error sit voluptatem accusantium doloremque laudantium, totam rem aperiam, eaque ipsa quae ab illo inventore veritatis et quasi architecto beatae vitae</p>
  </article>
  <article class="news-item">
    <div class="news-date">April 21th 2017</div>
    <h4>Sed ut perspiciatis unde omnis iste natus error sit voluptatem</h4>
    <div class="news-rule"></div>
    <p>Sed ut perspiciatis unde omnis iste natus error sit voluptatem accusantium doloremque laudantium, totam rem aperiam, eaque ipsa quae ab illo inventore veritatis et quasi architecto beatae vitae</p>
  </article>
</section>

<footer class="section footer">
  <div class="footer-brand"><span class="brand-dot"></span>VARLUK</div>
  <ul class="footer-col c1"><li>Home</li><li>Service</li><li>Projects</li><li>Finance</li><li>Solar</li></ul>
  <ul class="footer-col c2"><li>About</li><li>Solar Energy</li><li>News</li><li>Contacts</li><li>Social Media</li></ul>
  <ul class="footer-col c3"><li>Hallenwerk Studio</li><li>Lindorfer Straße 12</li><li>10437 Berlin</li><li>&nbsp;</li><li>E-Mail: info@varlukcorp.com</li></ul>
  <div class="footer-bottom">
    <span>© 2017 Company Name &nbsp;|&nbsp; All Rights Reserved</span>
    <span class="social">Connect With Us <i class="first"></i><i></i><i></i><i></i><i></i><i></i></span>
  </div>
</footer>

</body>
</html>
```